Tilda Tinkerwire, An IT Company Has New Logo, Need Fresh Business Cards

IT company is called Tilda Tinkerwire and is displayed nicely with the new logo from here on pitchloft. Would like a fresh business card look that encompasses the idea that we want clients to Cherish Every Gadget. I love the use of circuitry with hearts as endpoints and x's and o's. It needs to have room for my certification logos of which there are 4 and a BRJ Alumni log. I am attaching my current card to illustrate how it has always captured attention, but that was in the early stages of business when I was doing more residential work. I am focused on businesses now, so a level of professionalism is necessary. I would also like the card to lend itself well to additional stationary, email signature, ticketing template for my workboard, etc. For the time being, I need the card for an upcoming conference so that work will come later. Color scheme should be that of the new logo. Thank you and I look forward to the designs.

Target Market(s)

Businesses looking for IT services.

Industry/Entity Type

Information Technology

Contact Information for Business Card

See above

Requirements
Must have
• New logo colors and a warm feel. Possibly a tad feminine as I am female, but appealing to males.
Nice to have
• I would like techy, but no too much so. I like friendly and connecting feels. People LOVED my old card and called me because it gave them a warm feeling.

```html
<!DOCTYPE html>
<html lang="en">
<head>
<meta charset="utf-8">
<title>Tilda Tinkerwire – Business Card</title>
<link href="https://fonts.googleapis.com/css2?family=Questrial&display=swap" rel="stylesheet">
<style>
  :root {
    --page: #e9e6e1;
    --card-dark: #0b0b0c;
    --card-mid: #242427;
    --white: #ffffff;
    --blue: #7cc3e8;
    --green: #c6e27c;
    --pink: #f2a0c9;
    --badge: #3a3a3e;
    --badge-line: #7d7d84;
    --scene-a: #22566e;
    --scene-b: #e98a63;
  }
  * { box-sizing: border-box; margin: 0; padding: 0; }
  html, body { width: 1200px; height: 902px; overflow: hidden; }
  body {
    background: var(--page);
    font-family: "Questrial", "Century Gothic", sans-serif;
    position: relative;
  }
  .card {
    position: absolute;
    left: 40px; top: 132px;
    width: 1120px; height: 637px;
    background: radial-gradient(ellipse at 65% 40%, var(--card-mid) 0%, var(--card-dark) 70%);
    color: var(--white);
    overflow: hidden;
    box-shadow: 0 10px 30px rgba(0,0,0,.25);
  }

  /* Services */
  .services {
    position: absolute; right: 56px; top: 56px;
    text-align: right;
  }
  .services-title { font-size: 33px; line-height: 1; }
  .services-list {
    list-style: none;
    display: flex; gap: 26px; justify-content: flex-end;
    margin-top: 14px; font-size: 29px; line-height: 1;
  }
  .service { display: flex; align-items: center; gap: 8px; }
  .service svg { width: 32px; height: 30px; }
  .service--desktops { color: var(--blue); }
  .service--laptops { color: var(--green); }
  .service--tablets { color: var(--pink); }

  /* Identity block */
  .identity {
    position: absolute; left: 40px; top: 0;
    width: 540px; height: 520px;
    text-align: center;
  }
  .brand-mark {
    position: absolute; left: 194px; top: 42px;
    width: 150px; height: 150px; border-radius: 50%;
    border: 4px solid var(--pink);
  }
  .brand-name {
    position: absolute; left: 0; width: 540px; top: 226px;
    font-size: 52px; font-weight: 400; line-height: 1;
    color: var(--blue);
  }
  .tagline {
    position: absolute; left: 0; width: 540px; top: 282px;
    font-size: 17px; line-height: 1; letter-spacing: 5px;
    text-transform: uppercase; color: var(--pink);
  }
  .call {
    position: absolute; left: 0; width: 540px; top: 326px;
    font-size: 42px; line-height: 1;
  }
  .call-verb { color: var(--blue); }
  .call-name { color: var(--green); }
  .phone {
    position: absolute; left: 0; width: 540px; top: 376px;
    font-size: 31px; line-height: 1;
  }
  .email, .web {
    position: absolute; left: 0; width: 540px;
    font-size: 27px; line-height: 1;
  }
  .email { top: 442px; }
  .web { top: 472px; }
  .web-name { color: var(--pink); }

  /* Credentials row */
  .credentials {
    position: absolute; left: 38px; top: 532px;
    display: flex; gap: 12px; align-items: center;
  }
  .badge {
    display: block; height: 60px; border-radius: 6px;
    background: var(--badge); border: 2px solid var(--badge-line);
  }
  .badge--alumni { width: 90px; }
  .badge--cert { width: 112px; }
  .badge--cert-wide { width: 168px; }

  /* Illustration area */
  .illustration {
    position: absolute; left: 745px; top: 157px;
    width: 320px; height: 420px;
    border-radius: 12px;
    background: linear-gradient(160deg, var(--scene-b) 0%, var(--scene-a) 55%, #2c2c30 100%);
    opacity: .85;
  }
</style>
</head>
<body>
  <main class="card">
    <section class="services">
      <p class="services-title">Computer Care &amp; Repair</p>
      <ul class="services-list">
        <li class="service service--desktops">
          <svg viewBox="0 0 32 30" aria-hidden="true"><rect x="2" y="3" width="28" height="18" rx="1" fill="none" stroke="#fff" stroke-width="2.5"/><rect x="13" y="21" width="6" height="4" fill="#fff"/><rect x="8" y="25" width="16" height="2.5" fill="#fff"/></svg>
          Desktops
        </li>
        <li class="service service--laptops">
          <svg viewBox="0 0 32 30" aria-hidden="true"><rect x="5" y="6" width="22" height="15" rx="1" fill="none" stroke="#fff" stroke-width="2.5"/><path d="M1 24h30l-2 3H3z" fill="#fff"/></svg>
          Laptops
        </li>
        <li class="service service--tablets">
          <svg viewBox="0 0 32 30" aria-hidden="true"><rect x="8" y="2" width="16" height="26" rx="2" fill="none" stroke="#fff" stroke-width="2.5"/></svg>
          tablets
        </li>
      </ul>
    </section>

    <section class="identity">
      <span class="brand-mark" aria-hidden="true"></span>
      <h1 class="brand-name">TildaTinkerwire</h1>
      <p class="tagline">Cherish Every Gadget</p>
      <p class="call"><span class="call-verb">Call</span> <span class="call-name">Tilda!</span></p>
      <p class="phone">555-014-2873</p>
      <p class="email">tilda-tinkerwire@inboxly.com</p>
      <p class="web">www.<span class="web-name">tilda-tinkerwire</span>.com</p>
    </section>

    <section class="credentials" aria-label="Certifications and alumni">
      <span class="badge badge--alumni" aria-label="BRJ alumni badge"></span>
      <span class="badge badge--cert" aria-label="Certification badge"></span>
      <span class="badge badge--cert" aria-label="Certification badge"></span>
      <span class="badge badge--cert" aria-label="Certification badge"></span>
      <span class="badge badge--cert-wide" aria-label="Certification badge"></span>
    </section>

    <div class="illustration" role="img" aria-label="Illustration of a red-haired woman seated on a green chair, typing on a laptop at a wooden desk with a coffee cup"></div>
  </main>
</body>
</html>
```